Safety Work Area Signage to keep people away from work zone

We would like to create a simple design that will include our logo and phone number, 'work area', and 'caution / cuidado' (please see a mock-up of the intended design in the uploaded files). Please provide multiple options. We would like a Professional look for the poster as it is meant for safety. Poster Size to be: 18.16" X 23.10"

Target Market(s)

General Public on Construction Sites

Font styles to use
Serif

Requirements
Must have
• see mock-ups in uploaded files
Nice to have
• Simple Design, Professional Look

```html
<!DOCTYPE html>
<html lang="en">
<head>
<meta charset="utf-8">
<title>Caution Work Area Sign</title>
<link rel="stylesheet" href="https://fonts.googleapis.com/css2?family=Anton&family=Cinzel:wght@700&family=Oswald:wght@700&display=swap">
<style>
  :root {
    --backdrop: #8e8f91;
    --sign-white: #ffffff;
    --sky-light: #f4f9ff;
    --sky: #8cc6f5;
    --caution-red: #ff0000;
    --work-green: #006633;
    --phone-grey: #2f2f2f;
    --band-blue: #0070c9;
    --swoosh-dark: #3a3a3a;
    --swoosh-light: #e6e6e6;
    --brand-navy: #2b3a8f;
  }
  html, body {
    margin: 0;
    width: 1200px;
    height: 1200px;
    overflow: hidden;
    background: var(--backdrop);
  }
  .sign {
    position: absolute;
    left: 191px;
    top: 67px;
    width: 839px;
    height: 1066px;
    display: block;
  }
  .caution-title { font-family: "Anton", Impact, sans-serif; fill: var(--caution-red); }
  .work-area-title { font-family: "Cinzel", Georgia, serif; font-weight: 700; fill: var(--work-green); }
  .phone-number { font-family: "Oswald", Arial, sans-serif; font-weight: 700; fill: var(--phone-grey); }
  .cuidado-title { font-family: "Anton", Impact, sans-serif; fill: var(--sign-white); }
  .brand-name { font-family: "Cinzel", Georgia, serif; font-weight: 700; fill: var(--brand-navy); }
</style>
</head>
<body>
<svg class="sign" viewBox="0 0 839 1066" role="img" aria-label="Caution work area sign, Cuidado">
  <defs>
    <linearGradient id="sky-fill" x1="0" y1="0.6" x2="1" y2="0">
      <stop offset="0" stop-color="var(--sky-light)"/>
      <stop offset="1" stop-color="var(--sky)"/>
    </linearGradient>
    <linearGradient id="swoosh-fill" x1="0" y1="0" x2="1" y2="0">
      <stop offset="0" stop-color="var(--swoosh-dark)"/>
      <stop offset="0.5" stop-color="var(--swoosh-light)"/>
      <stop offset="1" stop-color="var(--swoosh-dark)"/>
    </linearGradient>
  </defs>

  <rect class="sign-face" width="839" height="1066" fill="var(--sign-white)"/>

  <path class="sky-band" fill="url(#sky-fill)"
        d="M0,0 H839 V240 C640,262 430,390 230,358 C130,342 50,310 0,282 Z"/>
  <path class="top-swoosh" fill="url(#swoosh-fill)"
        d="M90,332 C210,380 330,378 480,330 C620,286 740,252 839,238 V278 C740,288 620,334 480,372 C330,410 200,392 90,332 Z"/>

  <path class="bottom-swoosh" fill="url(#swoosh-fill)"
        d="M0,811 C150,772 320,800 470,848 C600,888 720,902 790,906 C700,916 600,906 470,896 C320,874 150,852 0,874 Z"/>
  <path class="blue-band" fill="var(--band-blue)"
        d="M0,880 C150,852 300,902 470,918 C650,936 760,912 839,894 V1066 H0 Z"/>

  <text class="caution-title" x="420" y="211" font-size="240" text-anchor="middle"
        textLength="720" lengthAdjust="spacingAndGlyphs">Caution</text>

  <g class="brand-seal">
    <circle cx="675" cy="317" r="88" fill="var(--sign-white)" stroke="var(--brand-navy)" stroke-width="5"/>
    <text class="brand-name" x="675" y="310" font-size="25" text-anchor="middle">
      <tspan x="675">Harbor &amp;</tspan>
      <tspan x="675" dy="32">Stone Co.</tspan>
    </text>
  </g>

  <text class="work-area-title" x="422" y="576" font-size="205" text-anchor="middle"
        textLength="701" lengthAdjust="spacingAndGlyphs">WORK</text>
  <text class="work-area-title" x="420" y="731" font-size="205" text-anchor="middle"
        textLength="600" lengthAdjust="spacingAndGlyphs">AREA</text>

  <text class="phone-number" x="420" y="814" font-size="68"
        textLength="391" lengthAdjust="spacingAndGlyphs">(555) 214-0387</text>

  <text class="cuidado-title" x="418" y="1028" font-size="132" text-anchor="middle"
        textLength="501" lengthAdjust="spacingAndGlyphs">Cuidado</text>
</svg>
</body>
</html>
```